Legislative compliance to home owners, landlords and agents

Logo, business card and stationaly header for a sole trader offering sevices in the UK to home owners, landlords and Letting agents to meet legislation requirement relating to sale and leasing of rental domestic homes. Services offered include Legionella Risk Assessment, Portable Appliance Testing and Energy Performance Certificates. Logo to include depiction of a house and compliance tick list images. Have an existing card with water splash image to reflect water testing, so considering picking up same wave blue. Company name Kestov Property Services. Web www.kestovps-example.com. email: info@kestovps-example.com. Address: Brackenlea, Aberdeen. All three services to be listed. Name as existing card.,

Target Market(s)

UK home owners, landlords, lettings and estate agents

Industry/Entity Type

Property Management

Contact Information for Business Card

Derek Moffatt CEng, MSFabTec
Address: Brackenlea, Aberdeen
Web: www.kestovps-example.com
e-mail info@kestovps-example.com
Phone: 07700 918 302
Services: Legionella Risk Assessment, Portable Appliance Testing, Energy Performance Certificate

Logo Text

Kestov Property Services

Font styles to use
Sans Serif

Colors

Designer to choose colors to be used in the design.

Requirements
Must have
• Suitable for standard UK business card size 85 mm x 55 mm, with allowance for safety border/ bleed such that colours extend to outside border of card once printed
Nice to have
• Clear font style and layout
• Happy to see images depicting phone, address etc

```html
<!DOCTYPE html>
<html lang="en">
<head>
<meta charset="utf-8">
<title>Kestov Property Services – Business Card</title>
<link rel="stylesheet" href="https://fonts.googleapis.com/css2?family=Lato:wght@400;700;900&display=swap">
<style>
  :root {
    --backdrop: #2b2b2d;
    --card: #f7f7f8;
    --navy: #1b1f72;
    --wave-blue: #2b9ed8;
    --ink: #1c1c1c;
    --white: #ffffff;
  }
  * { margin: 0; padding: 0; box-sizing: border-box; }
  html, body {
    width: 1200px; height: 997px; overflow: hidden;
    background: var(--backdrop);
    font-family: "Lato", Arial, sans-serif;
  }
  .business-card {
    position: absolute; left: 180px; top: 226px;
    width: 840px; height: 544px;
    background: var(--card);
    border-radius: 26px;
    overflow: hidden;
  }
  .card-bands { position: absolute; inset: 0; }
  .brand {
    position: absolute; left: 210px; top: 92px;
    display: flex; align-items: center; gap: 14px;
  }
  .brand-mark { width: 26px; height: 26px; background: var(--navy); }
  .brand-name {
    font-weight: 900; font-size: 36px; color: var(--navy); letter-spacing: 0.2px;
  }
  .divider {
    position: absolute; left: 90px; top: 168px; width: 700px; height: 2px;
    background: var(--navy);
  }
  .holder { position: absolute; left: 90px; top: 186px; }
  .holder-name {
    font-size: 26px; font-weight: 700; color: var(--navy);
    text-transform: uppercase; letter-spacing: 0.5px;
  }
  .holder-role { font-size: 21px; font-weight: 700; color: var(--wave-blue); margin-top: 2px; }
  .services {
    position: absolute; right: 44px; top: 192px; text-align: right; list-style: none;
  }
  .services-title {
    font-size: 20px; font-weight: 900; color: var(--navy); letter-spacing: 0.4px; margin-bottom: 4px;
  }
  .service {
    font-size: 19px; color: var(--wave-blue); line-height: 1.35;
    display: flex; justify-content: flex-end; align-items: center; gap: 6px;
  }
  .service svg { width: 14px; height: 14px; }
  .contact-tab {
    position: absolute; left: 0; top: 300px; width: 46px; height: 160px;
    background: var(--navy); border-radius: 0 12px 12px 0;
    display: flex; flex-direction: column; justify-content: space-around; align-items: center;
    padding: 10px 0;
  }
  .contact-tab svg { width: 20px; height: 20px; }
  .contacts { position: absolute; left: 92px; top: 314px; list-style: none; }
  .contact { font-size: 22px; color: var(--ink); line-height: 46px; }
  .website {
    position: absolute; right: 40px; bottom: 44px;
    font-size: 20px; color: var(--white); letter-spacing: 3px;
  }
</style>
</head>
<body>
  <article class="business-card">
    <svg class="card-bands" viewBox="0 0 840 544" width="840" height="544" aria-hidden="true">
      <path d="M0 510 L520 470 L520 544 L0 544 Z" fill="var(--wave-blue)"/>
      <path d="M480 544 C505 470 530 440 600 438 L840 426 L840 544 Z" fill="var(--navy)"/>
    </svg>

    <div class="brand">
      <span class="brand-mark"></span>
      <span class="brand-name">Kestov Property Services</span>
    </div>
    <div class="divider"></div>

    <div class="holder">
      <p class="holder-name">Derek Moffatt CEng, MSFabTec</p>
      <p class="holder-role">Director</p>
    </div>

    <ul class="services">
      <li class="services-title">SERVICES OFFERED</li>
      <li class="service">Legionella Risk Assessment
        <svg viewBox="0 0 14 14"><circle cx="6" cy="6" r="4" fill="none" stroke="var(--navy)" stroke-width="1.8"/><line x1="9" y1="9" x2="13" y2="13" stroke="var(--navy)" stroke-width="2"/></svg></li>
      <li class="service">Portable Appliance Testing
        <svg viewBox="0 0 14 14"><circle cx="6" cy="6" r="4" fill="none" stroke="var(--navy)" stroke-width="1.8"/><line x1="9" y1="9" x2="13" y2="13" stroke="var(--navy)" stroke-width="2"/></svg></li>
      <li class="service">Energy Performance Certificates
        <svg viewBox="0 0 14 14"><circle cx="6" cy="6" r="4" fill="none" stroke="var(--navy)" stroke-width="1.8"/><line x1="9" y1="9" x2="13" y2="13" stroke="var(--navy)" stroke-width="2"/></svg></li>
    </ul>

    <div class="contact-tab" aria-hidden="true">
      <svg viewBox="0 0 20 20"><path d="M3 6 Q3 3 6 3 L14 3 Q17 3 17 6 L15 8 L12 7 L12 5 L8 5 L8 7 L5 8 Z M5 10 L15 10 L16 17 L4 17 Z" fill="var(--white)"/></svg>
      <svg viewBox="0 0 20 20"><rect x="6" y="2" width="8" height="16" rx="1.5" fill="none" stroke="var(--white)" stroke-width="1.6"/><circle cx="10" cy="15" r="1" fill="var(--white)"/></svg>
      <svg viewBox="0 0 20 20"><rect x="3" y="5" width="14" height="10" rx="1" fill="var(--white)"/><path d="M3 5 L10 11 L17 5" fill="none" stroke="var(--navy)" stroke-width="1.4"/></svg>
    </div>

    <ul class="contacts">
      <li class="contact">07700 918 302</li>
      <li class="contact">info@kestovps-example.com</li>
      <li class="contact">Brackenlea, Aberdeen</li>
    </ul>

    <p class="website">www.kestovps-example.com</p>
  </article>
</body>
</html>
```